Legal Stationary

A full set of stationery is required
The image and logo, along with colour, are set and attached.
The style should be modern, clean, and corporate. Not just a basic template off the web.
In addition to the address/website/email/phone fields for KP and LCB number, with the text “the firm is authorised and regulated by the LCB”
All files in all formats will be needed to allow editing after. Initial setup of templates will be required, and details for 4 business cards will be supplied.
Consumers of legal services
Legal

```html
<!DOCTYPE html>
<html lang="en">
<head>
<meta charset="utf-8">
<title>Harrow Legal Stationery</title>
<link href="https://fonts.googleapis.com/css2?family=Mulish:wght@400;600&display=swap" rel="stylesheet">
<style>
:root{
  --brand-blue:#2c3f9c;
  --ink:#1f1f24;
  --charcoal:#2a2a2c;
  --paper:#ffffff;
  --rule:#8a8a92;
  --faint:#f1f2f7;
  --backdrop:#e8e5df;
}
*{box-sizing:border-box;margin:0;padding:0}
html,body{width:1200px;height:473px;overflow:hidden}
body{background:var(--backdrop);font-family:'Mulish',sans-serif;color:var(--ink);position:relative}
.sheet{position:absolute;top:45px;width:296px;height:382px;background:var(--paper);box-shadow:0 1px 4px rgba(0,0,0,.18);border-bottom:2px solid var(--charcoal)}
.letterhead{left:39px}
.fax-sheet{left:342px}
.sheet-header{height:34px;background:var(--brand-blue);position:relative}
.brand-name{font-family:'Mulish',sans-serif;font-weight:600;color:var(--paper);white-space:nowrap;letter-spacing:.2px}
.sheet-header .brand-name{position:absolute;left:11px;top:8px;font-size:15px}
.reg-info{position:absolute;right:7px;top:10px;text-align:right;color:var(--paper);font-size:4.8px;line-height:7.5px}
.watermark{position:absolute;left:11px;right:10px;top:297px;height:56px;background:var(--faint);display:flex;align-items:center;justify-content:center}
.watermark .brand-name{color:#e6e8f0;font-size:34px;font-weight:600}
.contact-footer{position:absolute;left:12px;right:12px;top:366px;display:flex;justify-content:space-between;font-size:4.5px;color:var(--ink)}
.contact-footer span{display:flex;align-items:center;gap:2px}
.icon{width:4.5px;height:4.5px;fill:var(--brand-blue)}
.fax-title{position:absolute;left:14px;top:55px;font-size:20px;line-height:24px;color:var(--brand-blue);font-weight:400}
.fax-fields{position:absolute;left:13px;right:16px;top:93px;display:grid;grid-template-columns:159px 1fr;row-gap:8px}
.fax-field{font-size:5.6px;line-height:6.5px;border-bottom:.6px solid var(--rule);height:8.5px}
.fax-options{position:absolute;left:13px;top:170px;width:270px;display:flex;justify-content:space-between;font-size:5.6px;line-height:7px}
.fax-options span{display:flex;align-items:center;gap:3px}
.checkbox{display:inline-block;flex:none;width:6.5px;height:6.5px;border:.7px solid var(--ink)}
.envelope{position:absolute;width:330px;height:148px;background:var(--paper);box-shadow:0 1px 4px rgba(0,0,0,.18);overflow:hidden}
.envelope-back-blue{left:822px;top:47px}
.envelope-back-dark{left:812px;top:112px;background:#f4f4f4}
.envelope-front{left:789px;top:186px;border-bottom:2px solid var(--brand-blue)}
.flap{position:absolute;left:0;top:0}
.flap-label{position:absolute;left:0;right:0;top:16px;text-align:center}
.flap-label .brand-name{font-size:19px}
.envelope-back-dark .brand-name{color:#b9b9bb}
.envelope-front .front-brand{position:absolute;left:8px;top:12px;font-size:21px;color:var(--brand-blue)}
.envelope-front .front-address{position:absolute;left:8px;top:43px;font-size:4.6px;display:flex;gap:2px;align-items:center}
.envelope-front .front-web{position:absolute;left:8px;bottom:7px;font-size:4.6px;letter-spacing:.4px;display:flex;gap:2px;align-items:center}
.envelope-front .side-mark{position:absolute;right:10px;top:10px;width:26px;height:128px;background:var(--faint);display:flex;align-items:center;justify-content:center}
.side-mark .brand-name{transform:rotate(-90deg);color:#e3e5ee;font-size:20px}
.card{position:absolute;top:357px;width:122px;height:69px;box-shadow:0 1px 3px rgba(0,0,0,.2);overflow:hidden}
.card-1{left:653px;background:var(--paper)}
.card-2{left:783px;background:var(--brand-blue)}
.card-3{left:913px;background:var(--charcoal)}
.card-4{left:1040px;background:var(--brand-blue)}
.card-band{position:absolute;left:0;right:0;top:0;height:26px;background:var(--brand-blue)}
.card .brand-name{position:absolute;left:0;right:0;text-align:center;font-size:12px}
.card-strip{position:absolute;left:0;right:0;bottom:0;height:6px;background:var(--charcoal);color:var(--paper);font-size:3.4px;text-align:center;line-height:6px}
.card-3 .card-strip{background:var(--brand-blue)}
.card-person{position:absolute;left:0;width:53px;top:32px;text-align:right;font-size:4.4px;color:var(--brand-blue)}
.card-person small{display:block;font-size:3px;color:#555}
.card-2 .card-person,.card-2 .card-person small,.card-2 .card-details{color:var(--paper)}
.card-details{position:absolute;left:62px;top:32px;font-size:3.4px;line-height:5px;color:var(--ink)}
.card-email{position:absolute;left:14px;top:53px;font-size:3.4px}
.card-2 .card-email{color:var(--paper)}
.card-divider{position:absolute;left:57px;top:32px;width:.5px;height:26px;background:#bbb}
.card-web{position:absolute;left:0;right:0;top:42px;text-align:center;color:var(--paper);font-size:4.2px;letter-spacing:.5px}
</style>
</head>
<body>

<svg width="0" height="0" style="position:absolute">
  <symbol id="pin" viewBox="0 0 10 10"><path d="M5 0a3.5 3.5 0 0 0-3.5 3.5C1.5 6 5 10 5 10s3.5-4 3.5-6.5A3.5 3.5 0 0 0 5 0zm0 5a1.4 1.4 0 1 1 0-2.8A1.4 1.4 0 0 1 5 5z"/></symbol>
  <symbol id="phone" viewBox="0 0 10 10"><path d="M2 1l2 2-1 1.5c.6 1.2 1.3 1.9 2.5 2.5L7 6l2 2-1.5 1.5C4 9 1 6 .5 2.5z"/></symbol>
  <symbol id="mail" viewBox="0 0 10 10"><path d="M0 2h10v6H0zm1 1v.4l4 2.6 4-2.6V3z"/></symbol>
  <symbol id="globe" viewBox="0 0 10 10"><path d="M5 0a5 5 0 1 0 0 10A5 5 0 0 0 5 0zm0 1c.7.8 1.2 2 1.3 3.5H3.7C3.8 3 4.3 1.8 5 1zM1 5.5h1.7c.1 1.3.4 2.4.9 3.2A4 4 0 0 1 1 5.5zm0-1a4 4 0 0 1 2.6-3.2c-.5.8-.8 1.9-.9 3.2zm4 4.5c-.7-.8-1.2-2-1.3-3.5h2.6C6.2 7 5.7 8.2 5 9zm1.4-.3c.5-.8.8-1.9.9-3.2H9a4 4 0 0 1-2.6 3.2zM7.3 4.5c-.1-1.3-.4-2.4-.9-3.2A4 4 0 0 1 9 4.5z"/></symbol>
</svg>

<section class="sheet letterhead">
  <header class="sheet-header">
    <span class="brand-name">Harrow Legal</span>
    <p class="reg-info">KP No. 7319048 &amp; LCB No. 582213<br>The Firm Is Authorised And Regulated By The LCB</p>
  </header>
  <div class="watermark"><span class="brand-name">Harrow Legal</span></div>
  <footer class="contact-footer">
    <span><svg class="icon"><use href="#pin"/></svg>Street Name, City Name, State Zipcode</span>
    <span><svg class="icon"><use href="#phone"/></svg>123.456.7890</span>
    <span><svg class="icon"><use href="#mail"/></svg>inquiry@harrowlegal.com</span>
    <span><svg class="icon"><use href="#globe"/></svg>www.harrowlegal.com</span>
  </footer>
</section>

<section class="sheet fax-sheet">
  <header class="sheet-header">
    <span class="brand-name">Harrow Legal</span>
    <p class="reg-info">KP No. 7319048 &amp; LCB No. 582213<br>The Firm Is Authorised And Regulated By The LCB</p>
  </header>
  <h1 class="fax-title">FAX</h1>
  <div class="fax-fields">
    <div class="fax-field">To :</div><div class="fax-field">From :</div>
    <div class="fax-field">Fax :</div><div class="fax-field">Pages :</div>
    <div class="fax-field">Phone :</div><div class="fax-field">Date :</div>
    <div class="fax-field">Re :</div><div class="fax-field">CC :</div>
  </div>
  <div class="fax-options">
    <span><i class="checkbox"></i>Urgent</span>
    <span><i class="checkbox"></i>For Review</span>
    <span><i class="checkbox"></i>Please Comment</span>
    <span><i class="checkbox"></i>Please Reply</span>
    <span><i class="checkbox"></i>Please Recycle</span>
  </div>
  <div class="watermark" style="top:292px"><span class="brand-name">Harrow Legal</span></div>
  <footer class="contact-footer">
    <span><svg class="icon"><use href="#pin"/></svg>Street Name, City Name, State Zipcode</span>
    <span><svg class="icon"><use href="#phone"/></svg>123.456.7890</span>
    <span><svg class="icon"><use href="#mail"/></svg>inquiry@harrowlegal.com</span>
    <span><svg class="icon"><use href="#globe"/></svg>www.harrowlegal.com</span>
  </footer>
</section>

<div class="envelope envelope-back-blue">
  <svg class="flap" width="330" height="70" viewBox="0 0 330 70"><path d="M0 0H330C326 30 300 34 180 56Q165 59 150 56C30 34 4 30 0 0Z" fill="var(--brand-blue)"/></svg>
  <div class="flap-label"><span class="brand-name">Harrow Legal</span></div>
</div>

<div class="envelope envelope-back-dark">
  <svg class="flap" width="330" height="70" viewBox="0 0 330 70"><path d="M0 0H330C326 30 300 34 180 56Q165 59 150 56C30 34 4 30 0 0Z" fill="var(--charcoal)"/></svg>
  <div class="flap-label"><span class="brand-name">Harrow Legal</span></div>
</div>

<div class="envelope envelope-front">
  <span class="brand-name front-brand">Harrow Legal</span>
  <p class="front-address"><svg class="icon"><use href="#pin"/></svg>Street Name, City Name, State Zipcode</p>
  <p class="front-web"><svg class="icon"><use href="#globe"/></svg>www.harrowlegal.com</p>
  <div class="side-mark"><span class="brand-name">Harrow Legal</span></div>
</div>

<article class="card card-1">
  <div class="card-band"></div>
  <span class="brand-name" style="top:6px">Harrow Legal</span>
  <p class="card-person">Your Name<small>Designation</small></p>
  <i class="card-divider"></i>
  <p class="card-details">Street Name, City Name<br>State Zipcode<br>123.456.7890<br>www.harrowlegal.com</p>
  <p class="card-email">inquiry@harrowlegal.com</p>
  <p class="card-strip">The Firm Is Authorised And Regulated By The LCB</p>
</article>

<article class="card card-2">
  <span class="brand-name" style="top:7px">Harrow Legal</span>
  <p class="card-person">Your Name<small>Designation</small></p>
  <p class="card-details">Street Name, City Name<br>State Zipcode<br>123.456.7890<br>www.harrowlegal.com</p>
  <p class="card-email">inquiry@harrowlegal.com</p>
  <p class="card-strip">The Firm Is Authorised And Regulated By The LCB</p>
</article>

<article class="card card-3">
  <span class="brand-name" style="top:23px">Harrow Legal</span>
  <p class="card-web">www.harrowlegal.com</p>
  <p class="card-strip">The Firm Is Authorised And Regulated By The LCB</p>
</article>

<article class="card card-4">
  <span class="brand-name" style="top:26px">Harrow Legal</span>
  <p class="card-strip">The Firm Is Authorised And Regulated By The LCB</p>
</article>

</body>
</html>
```